Digital Marketing Agency Needs a Pagecraft Web Design

We need a web design for a new company based in Evergreen, Colorado (the greater Denver Metro area) called "Copper Wayfarer". We are a full service Digital Marketing Agency that offers and provides the following services to clients: Website Design, Search Engine Optimization, Plexo Local Listing, Local Online Directories, Reputation Marketing, Social Media Marketing, Video Marketing, Pay Per Click. Our slogan is "Digital Marketing, Elevated!" We want a PageCraft web design that has a very modern look. We would like to see designs use the following colors (included color code):

light blue (#0cb9ea)
orange (#f47528)
white (#ffffff)
black (#000000).

These colors coincide with the colors of our logo (attached). We prefer a flat design but would like some elements of depth. We need a header that includes a logo (attached), name/address/phone number of our company, a contact call-to-action button (these need to be very easy to locate on the page), menu bar, and banner (very flexible to set up of banner).. The footer needs to include logo, NAP, Footer Menu, Section for blogs (includes title of blog that links to post), & copyright. We also need a way to prominently display and link our key featured services (Website Design, Search Engine Optimization, Plexo Local Listing, Local Online Directories, Reputation Marketing, Social Media Marketing, Video Marketing, Pay Per Click).

Here are three websites that we really like and would like to see certain elements incorporated:

1. http://quillstonemedia.example/ (like how the services were laid out on the home page for services -- "Features" section... want to follow this same type of idea, just in our own way).
2. http://tavenmark.example/ (love the modern, visual aspect of this site and how professionally clean it is.... very easy to understand and navigate through).
3. http://norvacreative.example/ (like how this site incorporates interactive features that engage people while visiting the site).

The overall goal of the site is to effectively emphasize the services we provide (see above), who we are, and how to contact us for services.

** Any stock photos used HAVE TO BE TAKEN from Lumafold Pictures (http://www.lumafoldpics.example/). And if watermarked, please provide the image code for each image used.

Target Market(s)

Lawyers, Insurance agents, Real Estate, Restaurant Owners, Doctors and all other medical providers.

Industry/Entity Type

Internet

Number of Pages Required

1 page

Font styles to use
Serif

Colors
33a6d7
ffffff
000000
f37122

Requirements
Must have
• 1. Header w/ Logo, Name/Address/Phone Number of our business, a call-to-action button to "Contact us":
• Copper Wayfarer – Digital Marketing
• 41872 Cobblewick Drive
• Evergreen, CO 80439
• 303-547-9183
• 2. Navigation Menu
• 3. Some type of banner
• 4. Featured Services section (with a short blurb about each)
• 5. Contact Form (somewhere above the fold)
• 6. Need at least 2-3 paragraphs of text (use dummy text) somewhere on the page (either in full or in sections)....
• 7. Footer that includes logo, NAP (see above), Menu Links, Links for services (see above), Blog Section, Social Media icons (Chatterly, Peepline, Plexo+, and ReelHub) & a copyright.
Nice to have
• Here are three websites that we really like and would be nice to see elements of incorporated:
• 1. http://quillstonemedia.example/ (like how the services were laid out on the home page -- "Features" section... want to follow this same type of idea, just in our own way).
• 2. http://tavenmark.example/ (love the modern, visual aspect of this site and how professionally clean it is.... very easy to understand and navigate through).
• 3. http://norvacreative.example/ (like how this site incorporates interactive features that engage people that visit the site).
Should not have
• Pretty flexible... We just need to make sure it's a Pagecraft web design.

```html
<!DOCTYPE html>
<html lang="en">
<head>
<meta charset="utf-8">
<title>Copper Wayfarer – Digital Marketing, Elevated!</title>
<link rel="stylesheet" href="https://fonts.googleapis.com/css2?family=Open+Sans:wght@300;400;600;700&family=Roboto+Condensed:wght@400;700&display=swap">
<style>
:root{
  --blue:#33a6d7;
  --sky:#0cb9ea;
  --orange:#f37122;
  --ink:#222222;
  --nav:#1f1f1f;
  --teal:#2bb6c4;
  --teal-dark:#16626d;
  --grey:#8a8a8a;
  --card:#eeeeee;
  --noimg:#cfcfcf;
  --footer:#efefef;
  --white:#ffffff;
}
*{box-sizing:border-box;margin:0;padding:0}
html,body{width:1200px;height:2528px;overflow:hidden}
body{position:relative;background:var(--white);font-family:"Open Sans",Arial,sans-serif;color:var(--ink)}
.abs{position:absolute}

/* top bar */
.topbar{left:0;top:0;width:1200px;height:40px;background:var(--blue);color:var(--white);font-size:12px;display:flex;align-items:center;justify-content:space-between;padding:0 100px}
.topbar .contact span{margin-right:28px}
.topbar .util{display:flex;align-items:center;gap:10px}
.dot-sm{width:14px;height:14px;border-radius:50%;background:rgba(255,255,255,.85);display:inline-block}

/* header */
.header{left:0;top:40px;width:1200px;height:108px;padding:0 100px;display:flex;align-items:center;justify-content:space-between}
.brand{display:flex;align-items:center;gap:14px}
.brand-mark{width:46px;height:46px;background:var(--orange);border-radius:50%}
.brand-name{font-size:34px;font-weight:700;color:var(--orange);line-height:1}
.brand-tag{font-size:12px;color:var(--blue);margin-top:4px;letter-spacing:.5px}
.nap{text-align:right}
.nap .phone{font-size:30px;color:var(--orange);font-weight:400}
.nap p{font-size:12px;color:var(--blue);line-height:1.5}

/* nav */
.nav{left:0;top:148px;width:1200px;height:38px;background:var(--nav);padding:0 100px;display:flex;align-items:center;gap:30px}
.nav a{color:var(--white);font-size:13px;text-decoration:none;font-weight:600;letter-spacing:.5px}

/* banner */
.banner{left:0;top:186px;width:1200px;height:474px;background:var(--teal)}
.banner-title{top:40px;left:0;width:1200px;text-align:center;font-family:"Roboto Condensed",Arial,sans-serif;font-size:44px;color:var(--white);letter-spacing:1px}
.banner-art{left:330px;top:110px;width:540px;height:280px;border-radius:8px;background:radial-gradient(circle at 50% 50%,#f59a52 0%,#e8e4dd 38%,#5fcbd5 75%,var(--teal) 100%)}
.banner-strip{left:0;top:406px;width:1200px;height:68px;background:var(--teal-dark);color:var(--white);font-family:"Roboto Condensed",Arial,sans-serif;font-size:42px;text-align:center;line-height:68px;letter-spacing:1px}

/* features */
.features-tab{left:100px;top:704px;width:52px;height:300px;background:var(--sky);display:flex;align-items:center;justify-content:center}
.features-tab span{transform:rotate(-90deg);color:var(--white);font-family:"Roboto Condensed",Arial,sans-serif;font-size:24px;font-weight:700;letter-spacing:4px;white-space:nowrap}
.features{left:164px;top:704px;display:flex;gap:10px}
.feature{width:108px;height:300px;background:var(--card)}
.feature .noimg{height:170px;background:var(--noimg);color:var(--white);font-size:15px;text-align:center;display:flex;align-items:center;justify-content:center;line-height:1.3}
.feature p{font-size:11px;color:#555;padding:12px 8px;line-height:1.45}
.pager{left:1036px;top:1040px;display:flex;gap:8px}
.pager i{width:12px;height:12px;border-radius:50%;background:#444;display:block}
.pager i.on{background:var(--orange)}

/* about / testimonials */
h2{font-weight:400;font-size:30px;color:var(--blue)}
h2 em{font-style:normal;color:var(--orange)}
.about{left:100px;top:1048px;width:460px}
.about p{font-size:14px;color:var(--grey);line-height:1.6;margin-top:14px}
.testimonials{left:630px;top:1048px;width:470px}
.testimonials h2{padding-left:22px}
.quote{display:flex;gap:14px;margin-top:12px}
.quote .mark{font-size:46px;color:var(--grey);line-height:.9;font-family:Georgia,serif}
.quote p{font-size:14px;color:var(--grey);line-height:1.6}
.quote .author{text-align:right;color:var(--orange);font-size:13px;font-weight:600;margin-top:4px}

/* portfolio */
.portfolio-title{left:100px;top:1372px}
.portfolio{left:100px;top:1432px;display:grid;grid-template-columns:repeat(3,320px);grid-auto-rows:208px;gap:28px 20px}
.portfolio div{border-radius:2px}

/* footer */
.footer{left:0;top:2192px;width:1200px;height:288px;background:var(--footer)}
.footer-cols{left:100px;top:2216px;width:1000px;display:grid;grid-template-columns:280px 220px 260px 240px}
.footer h3{font-size:20px;font-weight:400;color:var(--ink);margin-bottom:12px}
.footer ul{list-style:none}
.footer li{font-size:13px;color:var(--blue);line-height:1.55}
.footer .about-text{font-size:12px;color:var(--grey);line-height:1.5;margin-top:12px;width:230px}
.footer .brand-name{font-size:26px}
.footer .brand-mark{width:36px;height:36px}
.blog li{margin-bottom:8px}
.blog li span{display:block;color:var(--grey);font-size:12px}
.bottombar{left:0;top:2480px;width:1200px;height:48px;background:var(--blue);color:var(--white);font-size:12px;display:flex;align-items:center;justify-content:space-between;padding:0 100px}
.socials{display:flex;gap:10px}
.socials span{width:26px;height:26px;border-radius:50%;border:2px solid var(--white);display:block}
</style>
</head>
<body>

<div class="abs topbar">
  <div class="contact"><span>&#9742; 303-547-9183</span><span>&#9993; info@copperwayfarer.example</span></div>
  <div class="util"><span>Language</span><span>&#9662;</span><i class="dot-sm"></i><i class="dot-sm"></i></div>
</div>

<header class="abs header">
  <div class="brand">
    <div class="brand-mark"></div>
    <div>
      <div class="brand-name">Copper Wayfarer</div>
      <div class="brand-tag">Digital Marketing, Elevated!</div>
    </div>
  </div>
  <div class="nap">
    <div class="phone">(303) 547-9183</div>
    <p>Copper Wayfarer – Digital Marketing</p>
    <p>41872 Cobblewick Drive, Evergreen, CO 80439</p>
  </div>
</header>

<nav class="abs nav">
  <a href="#">HOME</a><a href="#">ABOUT US</a><a href="#">SERVICES</a><a href="#">TEAM</a><a href="#">WORK</a><a href="#">BLOG</a><a href="#">CONTACT</a>
</nav>

<section class="abs banner">
  <div class="abs banner-title">DIGITAL MARKETING TRENDS FOR 2015</div>
  <div class="abs banner-art" role="img" aria-label="Flat illustration of a megaphone surrounded by digital marketing icons above a city skyline"></div>
  <div class="abs banner-strip">DRIVING DIGITAL PERFORMANCE.</div>
</section>

<div class="abs features-tab"><span>FEATURES</span></div>
<section class="abs features">
  <div class="feature"><div class="noimg">NO<br>IMAGE</div><p>Website Design built for modern businesses</p></div>
  <div class="feature"><div class="noimg">NO<br>IMAGE</div><p>Search Engine Optimization that ranks</p></div>
  <div class="feature"><div class="noimg">NO<br>IMAGE</div><p>Plexo Local Listing setup and upkeep</p></div>
  <div class="feature"><div class="noimg">NO<br>IMAGE</div><p>Local Online Directories kept accurate</p></div>
  <div class="feature"><div class="noimg">NO<br>IMAGE</div><p>Reputation Marketing to grow trust</p></div>
  <div class="feature"><div class="noimg">NO<br>IMAGE</div><p>Social Media Marketing for your brand</p></div>
  <div class="feature"><div class="noimg">NO<br>IMAGE</div><p>Video Marketing that engages viewers</p></div>
  <div class="feature"><div class="noimg">NO<br>IMAGE</div><p>Pay Per Click campaigns that convert</p></div>
</section>
<div class="abs pager"><i class="on"></i><i class="on"></i><i></i><i></i></div>

<section class="abs about">
  <h2>About <em>Copper</em> Wayfarer</h2>
  <p>Donec sollicitudin molestie malesuada. Vestibulum ante ipsum primis in faucibus orci luctus et ultrices posuere cubilia.</p>
  <p>Auctor sit amet aliquam vel, ullamcorper sit amet ligula. Donec rutrum congue leo eget malesuada.</p>
  <p>Vivamus suscipit tortor eget felis porttitor volutpat. Curabitur arcu erat, accumsan id imperdiet et, porttitor at sem.</p>
</section>

<section class="abs testimonials">
  <h2>Testimonials</h2>
  <div class="quote">
    <div class="mark">&ldquo;</div>
    <div>
      <p>Donec sollicitudin molestie malesuada. Vestibulum ante ipsum primis in faucibus orci luctus et ultrices posuere.</p>
      <div class="author">John Doe</div>
    </div>
  </div>
</section>

<h2 class="abs portfolio-title">Our Portfolio</h2>
<section class="abs portfolio">
  <div role="img" aria-label="Website screenshot for a health and nutrition client" style="background:linear-gradient(160deg,#2e7d3a,#cfe3c8)"></div>
  <div role="img" aria-label="Website screenshot for a retail client" style="background:linear-gradient(160deg,#2a2a2a,#8c8c8c)"></div>
  <div role="img" aria-label="Photo of friends celebrating at a restaurant" style="background:linear-gradient(160deg,#c9a27c,#e8d6c4)"></div>
  <div role="img" aria-label="Website screenshot for an orthodontics client" style="background:linear-gradient(160deg,#1f6f9a,#9fd0e6)"></div>
  <div role="img" aria-label="Logo panel for an electronics client on a dark background" style="background:linear-gradient(160deg,#111,#3b3b3b)"></div>
  <div role="img" aria-label="Photo of computer hardware for a data backup client" style="background:linear-gradient(160deg,#3a3a3a,#b0b0b0)"></div>
  <div role="img" aria-label="Website screenshot for an outdoor adventure client" style="background:linear-gradient(160deg,#3d82c4,#b7d8ef)"></div>
  <div role="img" aria-label="Logo panel for a youth organisation on blue" style="background:#2196cf"></div>
  <div role="img" aria-label="Photo of a self storage facility with signage" style="background:linear-gradient(160deg,#1d3f7a,#9aa6b8)"></div>
</section>

<footer class="abs footer"></footer>
<div class="abs footer-cols footer">
  <div>
    <div class="brand">
      <div class="brand-mark"></div>
      <div><div class="brand-name">Copper Wayfarer</div><div class="brand-tag">Digital Marketing, Elevated!</div></div>
    </div>
    <p class="about-text">Donec sollicitudin molestie malesuada. Vivamus suscipit tortor eget felis porttitor. 41872 Cobblewick Drive, Evergreen, CO 80439 · 303-547-9183</p>
  </div>
  <div>
    <h3>Quick Links</h3>
    <ul><li>Home</li><li>About</li><li>Services</li><li>Team</li><li>Work</li><li>Blog</li><li>Contact</li></ul>
  </div>
  <div>
    <h3>Services</h3>
    <ul><li>Website Design</li><li>Search Engine Optimization</li><li>Plexo Local Listing</li><li>Local Online Directories</li><li>Reputation Marketing</li><li>Social Media Marketing</li><li>Video Marketing</li><li>Pay Per Click</li></ul>
  </div>
  <div class="blog">
    <h3>Blog</h3>
    <ul>
      <li>Local SEO Tips<span>Simple steps to rank in your town</span></li>
      <li>Review Strategy<span>Turn happy clients into five stars</span></li>
      <li>Video That Sells<span>Short clips that bring new leads</span></li>
    </ul>
  </div>
</div>

<div class="abs bottombar">
  <span>© 2015 Copper Wayfarer. All rights reserved. | Privacy | Terms of Use | Terms of Service</span>
  <div class="socials" aria-label="Chatterly, Peepline, Plexo+, ReelHub"><span></span><span></span><span></span><span></span></div>
</div>

</body>
</html>
```